1/4 page print add needed for local government consultancy entering new line of business.

We need a 1/4 page print ad for a trade conference program (Live Area of 3.75"x5") to help roll out a new consulting product intended for local governments in Texas. Our Bond Rating Assessment helps cities to maximize their Bond Rating and financial efficiency by lowering overall cost of debt-financed projects. Our audience is generally conservative and professional and about 90% male. Our company is the KVMoss Partners, LLC and I have attached our logo. We generally use bright blue tones, greys, and black in our other marketing material. Ad should cause people to go to www.kvmosspartners-example.com to get more information. Final product needs to be either PDF or JPEG at a minimum resolution of 300dpi.

After seeing some of the initial designs, I realize that while I want to highlight the Bond Rating Assessments, I need some more information about my business in the ad. I would also like to include a brief mention (probably title only) of my other lines of service: Economic Development Consulting, Executive Dashboards, Strategic Planning & Performance Management, Public Policy Analysis, and Governance Training. Thanks!

Target Market(s)

Highly educated professional public servants (City Managers). Generally stylistically conservative. Ad will run only in Texas, USA.

Industry/Entity Type

Government

Font styles to use
Sans Serif

Colors
0792cd

Requirements
Must have
• 1. Brief Description of Bond Rating Assessment service.
• 2. Call to action to visit www.kvmosspartners-example.com for more information.
• 3. Company logo (see attached)

```html
<!DOCTYPE html>
<html lang="en">
<head>
<meta charset="utf-8">
<title>KVMoss Partners – Bond Rating Assessment Ad</title>
<link rel="stylesheet" href="https://fonts.googleapis.com/css2?family=Montserrat:ital,wght@1,800&family=Questrial&display=swap">
<style>
  :root {
    --brand-blue: #0792cd;
    --ink: #000000;
    --paper: #ebebeb;
    --grey: #8a8a8a;
    --backdrop: #f4f4f4;
    --white: #ffffff;
  }
  html, body {
    margin: 0;
    width: 1200px;
    height: 750px;
    overflow: hidden;
    background: var(--backdrop);
    font-family: "Questrial", "Century Gothic", sans-serif;
  }
  .ad {
    position: absolute;
    left: 253px;
    top: 115px;
    width: 695px;
    height: 520px;
    background: var(--paper);
    color: var(--ink);
  }
  .headline {
    position: absolute;
    left: 0;
    right: 0;
    top: 4px;
    margin: 0;
    text-align: center;
    font-family: "Montserrat", "Arial Black", sans-serif;
    font-style: italic;
    font-weight: 800;
    font-size: 42px;
    line-height: 44px;
    letter-spacing: 0.32em;
  }
  .headline .line { display: block; }
  .headline .line--accent { color: var(--brand-blue); margin-left: -12px; }
  .column {
    position: absolute;
    top: 98px;
    width: 318px;
    font-size: 15px;
    line-height: 18.6px;
    text-align: justify;
  }
  .column p { margin: 0 0 5px; }
  .column strong { font-weight: 700; font-family: "Questrial", sans-serif; -webkit-text-stroke: 0.5px var(--ink); }
  .column--left { left: 22px; }
  .column--right { left: 358px; width: 320px; }
  .intro { color: var(--brand-blue); -webkit-text-stroke: 0.4px var(--brand-blue); }
  .contact {
    position: absolute;
    left: 340px;
    width: 345px;
    top: 330px;
    text-align: center;
  }
  .contact__label { color: var(--brand-blue); font-size: 18px; margin: 0; }
  .contact__phone {
    margin: 0 0 10px;
    font-family: "Montserrat", sans-serif;
    font-style: normal;
    font-weight: 800;
    font-size: 33px;
    letter-spacing: 0.02em;
  }
  .contact__email {
    margin: 0;
    font-size: 25px;
    -webkit-text-stroke: 0.8px var(--ink);
  }
  .brand {
    position: absolute;
    left: 68px;
    top: 368px;
    display: flex;
    align-items: center;
    gap: 12px;
    color: var(--grey);
    font-size: 34px;
    line-height: 1;
  }
  .brand__mark { width: 22px; height: 22px; background: var(--grey); }
  .brand__name small { display: block; font-size: 20px; margin-top: 4px; }
  .footer-band {
    position: absolute;
    left: 0;
    right: 0;
    bottom: 0;
    height: 46px;
    background: var(--ink);
    color: var(--white);
    text-align: center;
    font-size: 26px;
    line-height: 46px;
    -webkit-text-stroke: 0.8px var(--white);
    letter-spacing: 0.01em;
  }
</style>
</head>
<body>
  <section class="ad">
    <h1 class="headline">
      <span class="line">Confused about</span>
      <span class="line line--accent">Bond Ratings?</span>
    </h1>

    <div class="column column--left">
      <p class="intro">Our Assessment delivers the tools you need to maximize your community’s bond ratings.</p>
      <p><strong>The bond ratings system</strong> is confusing, at best. You know that you need to carry at least a 90-day General Fund reserve and manage your annual budget well.</p>
      <p><strong>Over the course of seven years</strong> as a City Manager, Kevin Moss helped two different communities increase bond ratings 4 times, including leading Millbrook, Texas to a top-rated AAA Ratewell’s rating during his tenure.</p>
    </div>

    <div class="column column--right">
      <p><strong>Our Bond Rating Assessment</strong> will provide you a detailed report on what the agencies are looking at, what their red flags may be, and we will provide advice on how to best communicate your community’s strengths to the analysts to ensure that you get the highest rating possible given your underlying financials. Then, we help prepare you and your financial team for the ratings calls, showing you exactly what to highlight as you represent the community.</p>
    </div>

    <div class="brand">
      <span class="brand__mark" aria-hidden="true"></span>
      <span class="brand__name">KVMoss Partners<small>LLC</small></span>
    </div>

    <div class="contact">
      <p class="contact__label">Find out more by calling</p>
      <p class="contact__phone">555-014-2290</p>
      <p class="contact__label">or email us at</p>
      <p class="contact__email">info@kvmosspartners-example.com</p>
    </div>

    <div class="footer-band">www.kvmosspartners-example.com</div>
  </section>
</body>
</html>
```